Business card for our large format printing and installation business

We want a professional looking business card for our business. We manufacture and install Signs.

On the back of the card add this info
Large Format Graphics Printing & Installations, Event Graphics, Banners, Posters, Vehicle Fleet Graphics, Boat Wraps, Wall Murals, Decals,Displays,Signs,Plaques,Digital Signs

On the Front of the card add the Tallowfern Signs logo, plus On the back of the card add the Orange Tallowfern Wraps logo. The 2 vector logos are attached to the design brief.

Target Market(s)

Local business owners

Contact Information for Business Card

Colors
f37122
f68d4e
f9ba93

Requirements
Must have
• On the Front of the card add the Tallowfern Signs logo, plus On the back of the card add the Orange Tallowfern Wraps logo. The 2 vector logos are attached to the design brief.

```html
<!DOCTYPE html>
<html lang="en">
<head>
<meta charset="utf-8">
<title>Tallowfern Signs – Business Card</title>
<link rel="stylesheet" href="https://fonts.googleapis.com/css2?family=Montserrat:wght@500;600;700;800&display=swap">
<style>
  :root {
    --orange: #f37122;
    --orange-mid: #f68d4e;
    --orange-light: #f9ba93;
    --ink: #1d1d1b;
    --paper: #ffffff;
    --stage: #e9e9e9;
    --accent-yellow: #ffd200;
  }
  * { box-sizing: border-box; margin: 0; padding: 0; }
  html, body { width: 1200px; height: 1200px; overflow: hidden; }
  body {
    background: var(--stage);
    font-family: "Montserrat", Arial, sans-serif;
    color: var(--ink);
    position: relative;
  }
  .card {
    position: absolute;
    left: 180px;
    width: 840px;
    height: 480px;
    box-shadow: 0 10px 28px rgba(0,0,0,.18);
    overflow: hidden;
  }

  /* Back side */
  .card-back {
    top: 90px;
    background: var(--orange);
    display: flex;
    flex-direction: column;
    align-items: center;
    justify-content: center;
  }
  .back-brand {
    font-weight: 800;
    font-size: 64px;
    letter-spacing: 1px;
    color: var(--ink);
    margin-bottom: 46px;
  }
  .services {
    text-align: center;
    font-weight: 800;
    text-transform: uppercase;
    color: var(--ink);
  }
  .services .line-main {
    font-size: 17px;
    line-height: 1.5;
    display: flex;
    align-items: center;
    justify-content: center;
    gap: 10px;
  }
  .services .marker {
    width: 0; height: 0;
    border-top: 6px solid transparent;
    border-bottom: 6px solid transparent;
    border-left: 10px solid var(--accent-yellow);
  }
  .services .marker.flip {
    border-left: 0;
    border-right: 10px solid var(--accent-yellow);
  }
  .services .line-small {
    margin-top: 6px;
    font-size: 11.5px;
    letter-spacing: .3px;
    display: inline-block;
    padding: 2px 10px;
    position: relative;
  }
  .services .line-small::before,
  .services .line-small::after {
    content: "";
    position: absolute;
    top: -4px; bottom: -6px;
    width: 6px;
    border: 2px solid var(--accent-yellow);
  }
  .services .line-small::before { left: -6px; border-right: 0; }
  .services .line-small::after { right: -6px; border-left: 0; }

  /* Front side */
  .card-front {
    top: 630px;
    background: var(--paper);
    border-bottom: 16px solid var(--orange);
    display: flex;
    align-items: center;
  }
  .front-brand {
    width: 400px;
    padding-left: 40px;
    font-weight: 800;
    font-size: 46px;
    line-height: 1.05;
    color: var(--orange);
  }
  .divider {
    width: 3px;
    height: 270px;
    background: var(--ink);
    margin: 0 40px 0 12px;
  }
  .contact .name {
    font-weight: 700;
    font-size: 40px;
  }
  .contact .role {
    font-weight: 600;
    font-size: 16px;
    margin-bottom: 26px;
  }
  .contact ul { list-style: none; }
  .contact li {
    display: flex;
    align-items: center;
    gap: 12px;
    font-weight: 500;
    font-size: 20px;
    line-height: 32px;
  }
  .contact li svg { width: 18px; height: 18px; fill: var(--orange); flex: none; }
</style>
</head>
<body>

<section class="card card-back" aria-label="Card back">
  <div class="back-brand">Tallowfern Wraps</div>
  <div class="services">
    <div class="line-main"><span class="marker"></span>Install Signs<span class="marker flip"></span></div>
    <div class="line-main"><span class="marker"></span>Large Format Graphics<span class="marker flip"></span></div>
    <div class="line-small">Vehicle wraps, wall murals, fleet graphics, event graphics, etc</div>
  </div>
</section>

<section class="card card-front" aria-label="Card front">
  <div class="front-brand">Tallowfern<br>Signs</div>
  <div class="divider"></div>
  <div class="contact">
    <div class="name">Mr Corwin</div>
    <div class="role">CEO</div>
    <ul>
      <li>
        <svg viewBox="0 0 24 24" aria-hidden="true"><path d="M6.6 10.8a15.1 15.1 0 0 0 6.6 6.6l2.2-2.2a1 1 0 0 1 1-.25 11.4 11.4 0 0 0 3.6.57 1 1 0 0 1 1 1V20a1 1 0 0 1-1 1A17 17 0 0 1 3 4a1 1 0 0 1 1-1h3.5a1 1 0 0 1 1 1c0 1.25.2 2.45.57 3.57a1 1 0 0 1-.25 1z"/></svg>
        1335 480 217
      </li>
      <li>
        <svg viewBox="0 0 24 24" aria-hidden="true"><path d="M6 3h12v5H6zM4 9h16a2 2 0 0 1 2 2v6h-4v4H6v-4H2v-6a2 2 0 0 1 2-2zm4 7v3h8v-3z"/></svg>
        02 9371 5064
      </li>
      <li>
        <svg viewBox="0 0 24 24" aria-hidden="true"><path d="M2 5h20v14H2zm2 2v.5l8 5.5 8-5.5V7zm0 3v7h16v-7l-8 5.5z"/></svg>
        mrcorwin@tallowfernsigns.com
      </li>
      <li>
        <svg viewBox="0 0 24 24" aria-hidden="true"><path d="M12 2a10 10 0 1 0 0 20 10 10 0 0 0 0-20zm0 2c.9 0 2.3 2.1 2.8 5H9.2C9.7 6.1 11.1 4 12 4zM4.3 11h4.8a16 16 0 0 0 .1 2H4.3a8 8 0 0 1 0-2zm10.6 0h4.8a8 8 0 0 1 0 2h-4.9a16 16 0 0 0 .1-2zM9.2 15h5.6c-.5 2.9-1.9 5-2.8 5s-2.3-2.1-2.8-5z"/></svg>
        www.tallowfernsigns.com
      </li>
    </ul>
  </div>
</section>

</body>
</html>
```